Exciting new vermouth brand needs a brilliant label!

We need a label design for an exciting new premium Italian Vermouth brand called Lunavera Vermouth.

Lunavera Vermouth is based on a recipe that has been handed down for four generations and is made in the traditional way in the Piedmonte region of Northern Italy.

Lunavera, which means 'heavenly' in Italian has been designed to elevate classic cocktails such as the Negroni, Americano and Manhattan with a base of Italian wine blended with botanicals such as wormwood, orange peel, rhubarb and cinchona. It has a delicately balanced bittersweet profile with hints of vanilla and citrus.

Its competitors include brands such as Vecchia Ricetta, Brunetti and Fabrizzi (see the uploaded brief for more examples).

The label is for a 50cl dark bottle (please refer to the uploaded brief) and should be based on maximum dimensions of 70mm (width) x 110mm (height). There is no limit to embellishments such as foil printing, embossing or any other premium finishes. The label does not necessarily need to be rectangular.

Feedback will be given quickly and constructively after submissions to ensure that the process is as fair and useful as possible for everyone.

Target Market(s)

25-45 year old Europeans, 50:50 female:male

Industry/Entity Type

Wine / Spirits / Vermouth

Requirements
Must have
• Fantastic design that is distinct from competitors, a premium feel and great lettering.
Should not have
• Generic images or patterns that do not relate to the brand (Lunavera) or the product

```html
<!DOCTYPE html>
<html lang="it">
<head>
<meta charset="utf-8">
<title>Lunavera Vermouth – Sweet Rosso Label</title>
<link rel="stylesheet" href="https://fonts.googleapis.com/css2?family=Josefin+Sans:wght@600;700&family=Marcellus&family=Oswald:wght@500&display=swap">
<style>
  :root {
    --backdrop: #000000;
    --gold: #b8935a;
    --gold-fold: #9c7a45;
    --gold-light: #f1edb7;
    --gold-mid: #d9bd80;
    --paper: #ffffff;
    --ink: #0b0b0b;
    --rosso: #de2b49;
    --rosso-deep: #b20a33;
    --azzurro: #0258c2;
    --cream: #ffffff;
  }
  html, body {
    margin: 0;
    padding: 0;
    width: 1200px;
    height: 1147px;
    overflow: hidden;
    background: var(--backdrop);
  }
  .label {
    display: block;
    width: 1200px;
    height: 1147px;
  }
  .tagline {
    font-family: "Marcellus", serif;
    font-size: 23px;
    fill: var(--ink);
    letter-spacing: -0.5px;
  }
  .ribbon-word {
    font-family: "Oswald", sans-serif;
    font-weight: 500;
    font-size: 34px;
    fill: var(--cream);
    letter-spacing: 1.5px;
  }
  .brand-name {
    font-family: "Josefin Sans", sans-serif;
    font-weight: 700;
    font-size: 92px;
    fill: var(--ink);
  }
  .variety {
    font-family: "Josefin Sans", sans-serif;
    font-weight: 600;
    font-size: 44px;
    fill: var(--cream);
    letter-spacing: 1px;
  }
  .serving {
    font-family: "Marcellus", serif;
    font-size: 40px;
    fill: var(--cream);
    letter-spacing: -1px;
  }
  .volume {
    font-family: "Marcellus", serif;
    font-size: 33px;
    fill: var(--cream);
  }
  .rule {
    stroke: var(--cream);
    stroke-width: 1;
    opacity: 0.8;
  }
</style>
</head>
<body>
<svg class="label" viewBox="0 0 1200 1147" xmlns="http://www.w3.org/2000/svg">
  <defs>
    <linearGradient id="gold-panel" x1="0" y1="0" x2="0" y2="1">
      <stop offset="0" stop-color="var(--gold-mid)"/>
      <stop offset="0.45" stop-color="var(--gold-light)"/>
      <stop offset="1" stop-color="var(--gold-mid)"/>
    </linearGradient>
    <linearGradient id="flourish-tone" x1="0" y1="0" x2="0" y2="1">
      <stop offset="0" stop-color="#c9a46a" stop-opacity="0.15"/>
      <stop offset="1" stop-color="#c9a46a" stop-opacity="0.35"/>
    </linearGradient>
    <clipPath id="rosso-clip">
      <polygon points="301,662 893,662 597,833"/>
    </clipPath>
    <path id="ribbon-arc" d="M507,489 Q597,461 687,489"/>
  </defs>

  <!-- outer gold frame -->
  <polygon class="frame" fill="var(--gold)"
           points="597,132 908,310 908,839 597,1017 285,839 285,310"/>

  <!-- gold ornament panels -->
  <polygon role="img" aria-label="Gilded baroque scrollwork panel" fill="url(#gold-panel)"
           points="597,147 893,319 893,655 301,655 300,319"/>

  <!-- blue lower field -->
  <polygon role="img" aria-label="Blue damask scrollwork field" fill="var(--azzurro)"
           points="300,662 893,662 893,830 597,1000 300,830"/>

  <!-- white pyramid -->
  <polygon class="pyramid" fill="var(--paper)" points="597,143 893,655 301,655"/>

  <!-- gold divider band -->
  <rect x="300" y="655" width="593" height="7" fill="var(--gold)"/>

  <!-- red chevron with sheen stripes -->
  <g clip-path="url(#rosso-clip)">
    <rect x="300" y="662" width="594" height="172" fill="var(--rosso)"/>
    <polygon fill="var(--rosso-deep)" points="300,668 894,676 894,682 300,688"/>
    <polygon fill="var(--rosso-deep)" points="300,700 894,716 894,722 300,716"/>
    <polygon fill="var(--rosso-deep)" points="300,738 894,744 894,750 300,752"/>
    <polygon fill="var(--rosso-deep)" points="300,770 894,776 894,780 300,782"/>
    <polygon fill="var(--rosso-deep)" points="300,796 894,806 894,810 300,806"/>
  </g>

  <!-- crest flourish -->
  <rect role="img" aria-label="Gold calligraphic flourish" x="517" y="276" width="160" height="90" rx="45"
        fill="url(#flourish-tone)"/>

  <!-- tagline -->
  <text class="tagline" x="597" y="401" text-anchor="middle">ANTICA RICETTA</text>
  <text class="tagline" x="597" y="424" text-anchor="middle">DI VERMOUTH PREGIATO</text>

  <!-- ribbon banner -->
  <g class="ribbon">
    <polygon class="ribbon-tail" fill="var(--gold)" points="453,499 493,490 493,528 453,537 465,518"/>
    <polygon class="ribbon-tail" fill="var(--gold)" points="741,499 701,490 701,528 741,537 729,518"/>
    <polygon class="ribbon-fold" fill="var(--gold-fold)" points="491,501 514,510 491,514"/>
    <polygon class="ribbon-fold" fill="var(--gold-fold)" points="703,501 680,510 703,514"/>
    <path class="ribbon-band" fill="var(--gold)" d="M491,460 Q597,420 703,460 L703,501 Q597,468 491,501 Z"/>
    <path d="M468,520 L493,514 L493,490" fill="none" stroke="var(--paper)" stroke-width="1.5"/>
    <path d="M726,520 L701,514 L701,490" fill="none" stroke="var(--paper)" stroke-width="1.5"/>
  </g>
  <text class="ribbon-word" text-anchor="middle">
    <textPath href="#ribbon-arc" startOffset="50%">VERMOUTH</textPath>
  </text>

  <!-- brand name -->
  <text class="brand-name" x="597" y="624" text-anchor="middle" textLength="440" lengthAdjust="spacingAndGlyphs">LUNAVERA</text>

  <!-- variety -->
  <text class="variety" x="597" y="726" text-anchor="middle">SWEET ROSSO</text>

  <!-- serving and volume -->
  <text class="serving" x="597" y="883" text-anchor="middle">SERVED CHILLED</text>
  <line class="rule" x1="537" y1="902" x2="657" y2="902"/>
  <text class="volume" x="597" y="935" text-anchor="middle">750 ml</text>
  <line class="rule" x1="537" y1="943" x2="657" y2="943"/>
</svg>
</body>
</html>
```